4.25" x 11" Door Hanger Design - Glass Bolt Internet Service

We are sourcing a door hanger that will be used to micro target specific neighborhoods with our new "Glass Bolt" internet service offering

This will be used as a template for a new type of plan we are offering in very specific areas. The first will be "Cedar Hollow" with 3 plan offerings.

Stock photos should be family friendly but we want something modern and exciting that we can use to advertise a new internet service offering.
Updates

Sorry if I missed this before, but we would of course like our website and phone number with an encouragement to call us Website: www.brivanet.example Phone: 555-304-2968

Target Market(s)

Residential Internet Service

Industry/Entity Type

Internet Service Provider

Font styles to use
Sans Serif
Other font styles liked:
• RockoFLF

Colors

Designer to choose colors to be used in the design.

Requirements
Must have
• 1) Our logo with "Internet Services" nearby to show "Brivanet Internet Services" (name and what we do)
• 2) "Glass Bolt Internet Service is Now Available in Cedar Hollow!"
• 3) Show three plans, we don't know the price yet and we will edit the winning design eventually when we know the exact price.
• 100 Mbps $XX.XX per month
• 250 Mbps $XX.XX per month
• 1 Gbps $XX.XX per month
• 4) The plan names and prices should be easy to edit in the future if/when we try these in different markets.
• This ad will be modified with specific information like prices and the location when we use it in specific spots.
• We will be using Printwagon for the printing, please use their website for the punch hole location, dimensions, etc.
• https://www.printwagon.example/door-hanger-printing/
Nice to have
• We want to demonstrate far higher than normal internet service speed offerings. This can use whatever you think demonstrates this idea to the customers better, something like a speed test looking logo
Should not have
• Do not copy our website, we want a fresh design

```html
<!DOCTYPE html>
<html lang="en">
<head>
<meta charset="utf-8">
<title>Brivanet Glass Bolt Door Hangers</title>
<link href="https://fonts.googleapis.com/css2?family=Roboto:wght@300;400;500&display=swap" rel="stylesheet">
<style>
  :root {
    --page: #ece8e1;
    --blue: #1784cc;
    --blue-deep: #0d4fa3;
    --navy: #0a1b55;
    --teal: #5ccbbd;
    --teal-deep: #1fb3a0;
    --panel-grey: #eef1f4;
    --white: #ffffff;
    --logo-blue: #3a9be0;
  }
  * { box-sizing: border-box; margin: 0; padding: 0; }
  html, body { width: 1200px; height: 1200px; overflow: hidden; }
  body {
    background: var(--page);
    font-family: "Roboto", Arial, sans-serif;
    position: relative;
  }
  .hanger {
    position: absolute;
    top: 85px;
    width: 397px;
    height: 1027px;
    overflow: hidden;
    background: linear-gradient(180deg, var(--blue) 0%, var(--blue) 55%, var(--blue-deep) 72%, var(--navy) 100%);
  }
  .hanger--front { left: 142px; }
  .hanger--back { left: 661px; }

  .hanger__hole {
    position: absolute;
    width: 124px; height: 124px;
    border-radius: 50%;
    background: var(--page);
    top: 37px;
  }
  .hanger__slit { position: absolute; top: 0; left: 0; width: 397px; height: 120px; }

  /* front */
  .front-panel {
    position: absolute;
    left: 20px; top: 0;
    width: 357px; height: 671px;
    background: var(--white);
    border-radius: 0 0 178px 178px;
  }
  .front-panel__top {
    position: absolute;
    left: 28px; top: 0;
    width: 341px; height: 174px;
    background: var(--panel-grey);
  }
  .headline-box {
    position: absolute;
    left: 30px; top: 174px;
    width: 336px; height: 155px;
    background: var(--teal);
    color: var(--white);
    text-align: center;
  }
  .headline-box__kicker {
    position: absolute; top: 18px; left: 0; right: 0;
    font-size: 26px; font-weight: 400;
    display: flex; align-items: center; justify-content: center; gap: 12px;
  }
  .headline-box__kicker::before, .headline-box__kicker::after {
    content: ""; width: 78px; height: 1px; background: var(--white);
  }
  .headline-box__name {
    position: absolute; top: 52px; left: 0; right: 0;
    font-size: 52px; font-weight: 400; letter-spacing: -1px; line-height: 1;
  }
  .headline-box__sub {
    position: absolute; top: 113px; left: 0; right: 0;
    font-size: 21px; font-weight: 400; letter-spacing: 4.5px;
  }
  .front-photo {
    position: absolute;
    left: 28px; top: 329px;
    width: 341px; height: 334px;
    border-radius: 0 0 170px 170px;
    background: linear-gradient(160deg, #e7e5e2 0%, #b9aa9c 45%, #4b6aa0 80%, #8a4a3c 100%);
  }
  .front-message {
    position: absolute; left: 0; right: 0; top: 716px;
    text-align: center; color: var(--white);
  }
  .front-message__lead { font-size: 25px; font-weight: 400; line-height: 1; }
  .front-message__place { font-size: 50px; font-weight: 400; line-height: 1; margin-top: 10px; letter-spacing: -0.5px; }
  .front-message__with { font-size: 25px; line-height: 1; margin-top: 10px; }
  .front-message__plans { font-size: 29px; line-height: 1; margin-top: 10px; }

  /* back */
  .back-photo-ring {
    position: absolute;
    left: -25px; top: 175px;
    width: 448px; height: 448px;
    border-radius: 50%;
    background: var(--teal-deep);
  }
  .back-photo {
    position: absolute;
    left: -15px; top: 185px;
    width: 428px; height: 428px;
    border-radius: 50%;
    background: linear-gradient(170deg, #f2f2f0 0%, #e8d9b0 35%, #e9cd3a 55%, #3a3f4a 75%, #8c9aa8 100%);
  }
  .plans {
    position: absolute; left: 10px; top: 665px;
    width: 377px; height: 112px;
    display: flex; justify-content: space-between;
  }
  .plan {
    width: 112px; height: 112px;
    border-radius: 50%;
    border: 2px solid var(--white);
    background: linear-gradient(180deg, #2ec3b6 0%, #1a8fb4 100%);
    color: var(--white);
    display: flex; flex-direction: column; align-items: center; justify-content: center;
    font-size: 17px; line-height: 1.15; font-weight: 400;
  }
  .plan-divider {
    position: absolute; top: 667px; width: 1px; height: 108px;
    background: rgba(255,255,255,0.5);
  }
  .contact {
    position: absolute; left: 36px; top: 805px;
    color: var(--white);
  }
  .contact__row { display: flex; align-items: center; gap: 14px; }
  .contact__phone { font-size: 46px; font-weight: 400; letter-spacing: -1px; line-height: 1; }
  .contact__web { font-size: 28px; font-weight: 400; line-height: 1; letter-spacing: -0.3px; }
  .contact__icon { width: 28px; height: 28px; flex: none; }

  /* footer shared */
  .footer {
    position: absolute; left: 0; bottom: 0;
    width: 397px; height: 132px;
  }
  .footer svg { position: absolute; left: 0; top: 0; }
  .brand {
    position: absolute; left: 0; right: 0; top: 60px;
    display: flex; align-items: center; justify-content: center; gap: 12px;
  }
  .brand__dot { width: 18px; height: 18px; border-radius: 50%; background: var(--logo-blue); }
  .brand__name { font-size: 52px; font-weight: 400; color: var(--logo-blue); letter-spacing: -1px; line-height: 1; }
  .footer__stripe {
    position: absolute; left: 0; bottom: 0; width: 397px; height: 6px;
    background: linear-gradient(90deg, var(--blue) 0 50%, var(--teal-deep) 50% 100%);
  }
</style>
</head>
<body>

<section class="hanger hanger--front">
  <div class="front-panel"></div>
  <div class="front-panel__top"></div>
  <div class="hanger__hole" style="left:148px;"></div>
  <svg class="hanger__slit" viewBox="0 0 397 120"><line x1="136" y1="0" x2="178" y2="45" stroke="var(--page)" stroke-width="4"/></svg>
  <div class="headline-box">
    <div class="headline-box__kicker">OUR NEW</div>
    <div class="headline-box__name">GLASS BOLT</div>
    <div class="headline-box__sub">SERVICE OFFERING</div>
  </div>
  <div class="front-photo" role="img" aria-label="Family photo: parents and two children smiling at a laptop on a sofa"></div>
  <div class="front-message">
    <div class="front-message__lead">THE FIRST WILL BE</div>
    <div class="front-message__place">CEDAR HOLLOW</div>
    <div class="front-message__with">WITH</div>
    <div class="front-message__plans">3 PLAN OFFERINGS</div>
  </div>
  <div class="footer">
    <svg width="397" height="132" viewBox="0 0 397 132"><path d="M0 0 Q198 66 397 0 L397 132 L0 132 Z" fill="var(--white)"/></svg>
    <div class="brand"><span class="brand__dot"></span><span class="brand__name">Brivanet</span></div>
    <div class="footer__stripe"></div>
  </div>
</section>

<section class="hanger hanger--back">
  <div class="back-photo-ring"></div>
  <div class="back-photo" role="img" aria-label="Family photo: father with laptop on a yellow sofa, mother and young daughter looking on"></div>
  <div class="hanger__hole" style="left:125px;"></div>
  <svg class="hanger__slit" viewBox="0 0 397 120"><line x1="270" y1="0" x2="228" y2="45" stroke="var(--page)" stroke-width="4"/></svg>
  <div class="plans">
    <div class="plan"><span>100 Mbps</span><span>$ 50</span><span>Per Month</span></div>
    <div class="plan"><span>250 Mbps</span><span>$ 100</span><span>Per Month</span></div>
    <div class="plan"><span>1 Gbps</span><span>$ 300</span><span>Per Month</span></div>
  </div>
  <div class="plan-divider" style="left:133px;"></div>
  <div class="plan-divider" style="left:265px;"></div>
  <div class="contact">
    <div class="contact__row">
      <svg class="contact__icon" viewBox="0 0 24 24"><path d="M6.6 10.8a15 15 0 0 0 6.6 6.6l2.2-2.2a1 1 0 0 1 1-.25 11 11 0 0 0 3.6.6 1 1 0 0 1 1 1V20a1 1 0 0 1-1 1A17 17 0 0 1 3 4a1 1 0 0 1 1-1h3.5a1 1 0 0 1 1 1 11 11 0 0 0 .6 3.6 1 1 0 0 1-.25 1z" fill="none" stroke="var(--white)" stroke-width="1.6"/><path d="M15 3a6 6 0 0 1 6 6M15 6.5a2.5 2.5 0 0 1 2.5 2.5" fill="none" stroke="var(--white)" stroke-width="1.6"/></svg>
      <span class="contact__phone">555-304-2968</span>
    </div>
    <div class="contact__row" style="margin-top:8px;">
      <svg class="contact__icon" viewBox="0 0 24 24"><circle cx="12" cy="12" r="11" fill="none" stroke="var(--white)" stroke-width="1.4"/><circle cx="12" cy="12" r="6.5" fill="none" stroke="var(--white)" stroke-width="1.2"/><ellipse cx="12" cy="12" rx="2.8" ry="6.5" fill="none" stroke="var(--white)" stroke-width="1.1"/><path d="M5.5 12h13M6.5 9h11M6.5 15h11" stroke="var(--white)" stroke-width="1"/></svg>
      <span class="contact__web">www.brivanet.example</span>
    </div>
  </div>
  <div class="footer">
    <svg width="397" height="132" viewBox="0 0 397 132"><path d="M0 0 Q198 66 397 0 L397 132 L0 132 Z" fill="var(--white)"/></svg>
    <div class="brand"><span class="brand__dot"></span><span class="brand__name">Brivanet</span></div>
    <div class="footer__stripe"></div>
  </div>
</section>

</body>
</html>
```